Business Card for plorvaTEC

Create a Business Card with an existing logo for plorvaTEC AG. We are a Information Technology company that does consulting and developing SW to automate business processes. The main colors are given from the logo.

Industry/Entity Type

Business

Requirements
Nice to have
• we use a a font style Century Gothic in our documents

```html
<!DOCTYPE html>
<html lang="en">
<head>
<meta charset="utf-8">
<title>plorvaTEC AG – Business Card</title>
<link rel="stylesheet" href="https://fonts.googleapis.com/css2?family=Didact+Gothic&family=Arimo:wght@700&display=swap">
<style>
  :root {
    --page-bg: #e6e8eb;
    --blue-deep: #1d4fa6;
    --green: #7cc242;
    --yellow-label: #f3e41c;
    --ink-grey: #4a4a4a;
    --name-blue: #1f5fb4;
    --bar-grey: #c9c9c9;
    --text-white: #ffffff;
  }
  * { margin: 0; padding: 0; box-sizing: border-box; }
  html, body { width: 1200px; height: 800px; overflow: hidden; }
  body {
    background: var(--page-bg);
    font-family: "Didact Gothic", "Century Gothic", sans-serif;
  }
  .canvas { position: relative; width: 1200px; height: 800px; }
  .business-card {
    position: absolute;
    left: 120px;
    top: 120px;
    width: 960px;
    height: 560px;
    box-shadow: 0 14px 40px rgba(0,0,0,0.25);
    overflow: hidden;
  }
  .card-art { position: absolute; inset: 0; }
  .brand {
    position: absolute;
    left: 200px;
    top: 52px;
    display: flex;
    align-items: center;
    gap: 18px;
  }
  .brand-dot { width: 58px; height: 58px; border-radius: 50%; background: var(--green); }
  .brand-name {
    font-size: 58px;
    color: var(--ink-grey);
    letter-spacing: -1px;
    line-height: 1;
  }
  .person {
    position: absolute;
    right: 170px;
    top: 220px;
    text-align: right;
    font-family: "Arimo", Arial, sans-serif;
  }
  .person-name { font-size: 30px; font-weight: 700; color: var(--name-blue); letter-spacing: 0.5px; }
  .person-bar {
    height: 14px;
    width: 230px;
    margin: 2px 0 0 auto;
    background: linear-gradient(90deg, rgba(201,201,201,0.2), var(--bar-grey));
  }
  .person-role { font-size: 22px; font-weight: 700; color: var(--ink-grey); margin-top: 2px; }
  .phones {
    position: absolute;
    left: 62px;
    top: 318px;
    font-size: 20px;
    line-height: 34px;
    color: var(--text-white);
  }
  .phones .label { color: var(--yellow-label); }
  .divider {
    position: absolute;
    left: 420px;
    top: 420px;
    width: 1px;
    height: 118px;
    background: rgba(255,255,255,0.55);
  }
  .contacts {
    position: absolute;
    left: 446px;
    top: 428px;
    list-style: none;
    font-size: 19px;
    color: var(--text-white);
  }
  .contacts li { display: flex; align-items: center; gap: 14px; height: 34px; white-space: nowrap; }
  .contacts svg { width: 20px; height: 20px; flex: none; }
</style>
</head>
<body>
<main class="canvas">
  <section class="business-card" aria-label="plorvaTEC AG business card">
    <svg class="card-art" viewBox="0 0 960 560" preserveAspectRatio="none" aria-hidden="true">
      <defs>
        <linearGradient id="blueField" x1="0" y1="0" x2="1" y2="1">
          <stop offset="0" stop-color="#1d4fa6"/>
          <stop offset="0.55" stop-color="#2a78cf"/>
          <stop offset="1" stop-color="#3fa0e4"/>
        </linearGradient>
        <linearGradient id="greenSweep" x1="0" y1="0" x2="1" y2="0">
          <stop offset="0" stop-color="#7cc242"/>
          <stop offset="0.7" stop-color="#8cc63f"/>
          <stop offset="1" stop-color="#d6e21e"/>
        </linearGradient>
      </defs>
      <rect class="blue-field" width="960" height="560" fill="url(#blueField)"/>
      <path class="corner-band" d="M790 0 C875 110 935 250 960 380" fill="none" stroke="#7cc242" stroke-width="12"/>
      <path class="corner-band" d="M820 0 C900 100 950 210 960 280" fill="none" stroke="#3fa0e4" stroke-width="20"/>
      <path class="white-panel" d="M0 0 H760 C840 110 885 250 905 398 C600 388 300 300 0 160 Z" fill="#ffffff"/>
      <path class="sweep-band" d="M0 172 C300 312 600 402 960 412" fill="none" stroke="url(#greenSweep)" stroke-width="14"/>
      <path class="sweep-line" d="M0 190 C300 330 600 420 960 430" fill="none" stroke="#d6e21e" stroke-width="4"/>
      <path class="panel-edge" d="M760 0 C840 110 885 250 905 398" fill="none" stroke="#7cc242" stroke-width="8"/>
    </svg>

    <div class="brand">
      <span class="brand-dot"></span>
      <span class="brand-name">plorvaTEC</span>
    </div>

    <div class="person">
      <div class="person-name">LUKAS BRENNER</div>
      <div class="person-bar"></div>
      <div class="person-role">CEO</div>
    </div>

    <div class="phones">
      <div><span class="label">Office:</span> +41 56 500 18 40</div>
      <div><span class="label">Cell:</span> +41 79 600 27 55</div>
    </div>

    <div class="divider"></div>

    <ul class="contacts">
      <li>
        <svg viewBox="0 0 20 20"><rect x="2" y="4" width="16" height="12" rx="1.5" fill="#f3e41c"/><path d="M2.5 5 L10 11 L17.5 5" fill="none" stroke="#1d4fa6" stroke-width="1.5"/></svg>
        lukas.brenner@plorvatec.ch
      </li>
      <li>
        <svg viewBox="0 0 20 20"><circle cx="10" cy="10" r="8" fill="none" stroke="#f3e41c" stroke-width="2"/><ellipse cx="10" cy="10" rx="3.5" ry="8" fill="none" stroke="#f3e41c" stroke-width="1.5"/><line x1="2" y1="10" x2="18" y2="10" stroke="#f3e41c" stroke-width="1.5"/></svg>
        www.plorvatec.ch
      </li>
      <li>
        <svg viewBox="0 0 20 20"><path d="M10 1 C5.5 1 3 4.3 3 7.6 C3 12 10 19 10 19 C10 19 17 12 17 7.6 C17 4.3 14.5 1 10 1 Z" fill="#f3e41c"/><circle cx="10" cy="7.6" r="2.6" fill="#1d4fa6"/></svg>
        Lindenweg 12, 5400 Baden, Switzerland
      </li>
    </ul>
  </section>
</main>
</body>
</html>
```